Website Design Chair in Commercial Studies, especially data and operations networks

We, the Chair in Commercial Studies, especially data and operations networks, teach in the field of Business Informatics and Business Administration at Vellmoor University.
We want to setup our current website in a fresh new and clean design because the design of the old page is outdated: http://dkn.uni-vellmoor.example/en/
The design should be created in a way that we can integrate it into Wordpress later. Furthermore, the website should have the existing website tabs (pages). We want to add the missing subcategories in the tabs, which means that when you move the mouse over a tab, subcategories/side menus should appear.
We have the goal that the website is very clear and that the students get a direct overview especially of the lectures offered. Furthermore the website should be suitable for mobile devices.
Start page:
In general we are interested in a Tile-based Design (2 or more columns) on the start page - similar to this page: https://www.uni-brt.example/. Here, the fields (Data and Operations Networks (DKN) with photo, Lectures of the semester, theses, study projects, projects, current events (social media wall), jobs and internship (together), new publications) should be integrated in the form of tiles with a cover picture per field and a short description.
Furthermore, we would like to position a search bar, a social media wall especially for Instagram (replaces the field current events) and the cooperation partners perhaps as sliders with logos of the companies in the lower part of the start page (see Cooperation tab on the far right) on the start page. Footer remains the same.
Research:
Display the same content more attractively.
Learning-Platform:
Furthermore only as link.
Teaching:
In addition to the existing sub-items (Lectures of the semester, teaching-archive, learning platform, theses and book lending), the "Overview of DKN courses" and the " Open Bachelor & Master theses" should be graphically displayed.
Team:
The concept of the Teamgraph including project connections should remain. Furthermore we can imagine to list the employees with photos and short description in form of tiles (1 employee on a tile) below the graph (2 or more columns of tiles).
Publications:
Continue to display a list of publications.
Jobs and internships:
The Open Positions should be divided here into Research Associates, Student Assistants and interns, so that it becomes clearer (3 columns).
Projects:
Here we are interested a Tile-based Design (2 or more columns). We want to integrate the project fields (PLONTIX, Bright Record Holdings etc.) in the form of tiles with a title image per field and a short description.
Events and cooperations should be removed as they are sufficiently represented on the start page.
Target Market(s)
Students as well as current and future project partners
Logo Text
DKN (+ optional Chair in Data and Operations Networks)
Coding
Coded - Design and coding required
Number of Pages Required
5+ page
Requirements
Must have
- See description above
Nice to have
- Perhaps a design can be created in which a direct connection to research content (AI, Deep Learning etc.) and to courses (Data Science, AI in companies etc.) can be seen.

```html
<!DOCTYPE html>
<html lang="en">
<head>
<meta charset="utf-8">
<title>DKN – Data and Operations Networks</title>
<link href="https://fonts.googleapis.com/css2?family=Montserrat:wght@500;600;700;800&family=Open+Sans:wght@400;600;700&display=swap" rel="stylesheet">
<style>
:root{
  --navy:#1b3a72;
  --navy-dark:#15326b;
  --red:#e5432b;
  --blush:#f4efef;
  --mist:#ececef;
  --ink:#333a45;
  --muted:#555c66;
  --line:#cfd2d8;
  --link:#2a5ea3;
}
*{box-sizing:border-box;margin:0;padding:0}
html,body{width:1200px;height:5213px;overflow:hidden}
body{font-family:"Open Sans",Arial,sans-serif;color:var(--ink);background:#fff;position:relative}
section,header,footer{position:absolute;left:0;width:1200px}
.abs{position:absolute}
h2.section-title{font-family:"Montserrat",Arial,sans-serif;font-weight:800;color:var(--navy);font-size:22px;letter-spacing:.3px}
.btn{position:absolute;background:var(--red);color:#fff;font-family:"Montserrat",Arial,sans-serif;font-weight:700;font-size:12px;letter-spacing:.4px;display:flex;align-items:center;justify-content:center;text-transform:uppercase}
.caret-list{list-style:none;position:absolute}
.caret-list li{position:relative;padding-left:18px;font-size:14px;color:var(--ink)}
.caret-list li::before{content:"";position:absolute;left:2px;top:50%;margin-top:-5px;border-left:6px solid var(--navy);border-top:5px solid transparent;border-bottom:5px solid transparent}
.photo{position:absolute}

/* header */
.site-header{top:0;height:79px;background:#fff}
.brand{position:absolute;left:134px;top:14px;display:flex;align-items:center;gap:10px}
.brand-dot{width:48px;height:48px;border-radius:50%;background:var(--navy)}
.brand-name{font-family:"Montserrat",Arial,sans-serif;font-weight:700;font-size:38px;color:var(--navy);letter-spacing:1px}
.main-nav{position:absolute;top:31px;font-family:"Montserrat",Arial,sans-serif;font-weight:600;font-size:13px;color:#222}
.social{position:absolute;top:28px;width:24px;height:24px;border-radius:50%;background:var(--navy)}

/* hero */
.hero{top:79px;height:522px;background:linear-gradient(180deg,#8f8a86 0%,#6e6763 45%,#3e3a3a 100%)}
.hero-title{position:absolute;top:60px;width:1200px;text-align:center;font-family:"Montserrat",Arial,sans-serif;font-weight:800;font-size:33px;color:#fff;text-shadow:0 2px 6px rgba(0,0,0,.35)}
.dot{position:absolute;top:475px;width:7px;height:7px;border-radius:50%;background:#fff}
.dot.active{width:11px;height:11px;top:473px;background:var(--red);border:2px solid #fff}

/* about */
.about{top:601px;height:478px;background:var(--blush)}
.about-title{position:absolute;left:636px;top:46px;font-size:22px;line-height:31px}
.about-text{position:absolute;left:636px;top:150px;width:428px;font-size:12.5px;line-height:20px;color:var(--ink)}

/* research */
.research{top:1079px;height:481px;background:#fff}

/* teaching */
.teaching{top:1560px;height:304px;background:var(--blush)}
.field{position:absolute;background:#fff;border:1px solid var(--line);font-size:12px;color:#333;display:flex;align-items:center;padding:0 14px;justify-content:space-between}

/* team */
.team{top:1864px;height:830px;background:#fff}
.team h3{font-family:"Open Sans",Arial,sans-serif;font-weight:400;font-size:21px;color:#222;position:absolute}
.team p.body{position:absolute;left:134px;width:934px;font-size:13px;line-height:20.5px;color:#333}
.contact-item{position:absolute;display:flex;gap:12px;align-items:center;font-size:13px;line-height:18px;color:#222}
.icon-circle{width:28px;height:28px;border-radius:50%;background:var(--navy);display:flex;align-items:center;justify-content:center}

/* publications */
.publications{top:2694px;height:409px;background:var(--mist)}
.pub-card{position:absolute;top:126px;width:302px;height:228px;background:#fff;padding:30px 8px 30px 34px}
.pub-card h4{font-family:"Montserrat",Arial,sans-serif;font-size:11.5px;font-weight:700;color:#222;margin-bottom:16px;white-space:nowrap}
.pub-card p{font-size:11px;line-height:17px;color:#333;width:240px}
.pdf-tag{position:absolute;left:34px;bottom:30px;border:1px solid #bbb;font-size:10px;padding:3px 8px;color:#444}

/* projects */
.projects{top:3103px;height:641px;background:#fff}
.proj-sub{position:absolute;top:158px;font-family:"Montserrat",Arial,sans-serif;font-weight:800;font-size:16px;color:#111}
.proj-box{position:absolute;top:194px;width:454px;height:389px;border:1px solid var(--line);box-shadow:0 2px 8px rgba(0,0,0,.06)}
.proj-item{position:absolute;left:32px;width:388px}
.proj-item h4{font-family:"Montserrat",Arial,sans-serif;font-weight:700;font-size:12.5px;color:#222;padding-left:22px;position:relative}
.proj-item h4::before{content:"";position:absolute;left:2px;top:2px;border-left:6px solid var(--navy);border-top:5px solid transparent;border-bottom:5px solid transparent}
.proj-item p{font-size:11px;line-height:17px;color:#333;margin:10px 0 6px 22px}
.proj-item a{margin-left:22px;font-family:"Montserrat",Arial,sans-serif;font-weight:700;font-size:9.5px;color:var(--red);text-decoration:underline}
.proj-rule{position:absolute;left:54px;width:366px;height:1px;background:var(--line)}

/* news */
.news{top:3744px;height:569px;background:var(--mist)}
.news-card{position:absolute;top:128px;width:302px;height:385px;background:#fff}
.news-card .photo{left:0;top:0;width:302px;height:186px}
.news-body{position:absolute;left:22px;top:204px;width:262px}
.news-date{font-size:10.5px;font-weight:700;color:#222;margin-bottom:8px}
.news-body h4{font-family:"Open Sans",Arial,sans-serif;font-weight:700;font-size:13px;line-height:17px;color:#111;margin-bottom:10px}
.news-body p{font-size:11px;line-height:16px;color:#333}

/* jobs */
.jobs{top:4313px;height:555px;background:#fff}
.jobs-text{position:absolute;left:719px;top:172px;width:350px;font-size:14px;line-height:21.5px;color:#444}

/* footer */
.site-footer{top:4868px;height:345px;background:var(--navy-dark);color:#fff}
.footer-head{position:absolute;top:56px;font-family:"Montserrat",Arial,sans-serif;font-weight:700;font-size:11.5px}
.footer-text{position:absolute;font-size:11.5px;line-height:15.5px;color:#fff}
.footer-menu{position:absolute;list-style:none;font-size:11px;line-height:20px;text-transform:uppercase}
.copyright{position:absolute;top:302px;width:1200px;text-align:center;font-size:9.5px;color:#dfe4ee}
</style>
</head>
<body>

<header class="site-header">
  <div class="brand"><span class="brand-dot"></span><span class="brand-name">DKN</span></div>
  <span class="main-nav" style="left:310px">RESEARCH</span>
  <span class="main-nav" style="left:411px">TEACHING</span>
  <span class="main-nav" style="left:510px">TEAM</span>
  <span class="main-nav" style="left:585px">PUBLICATIONS</span>
  <span class="main-nav" style="left:718px">PROJECTS</span>
  <span class="main-nav" style="left:820px">NEWS</span>
  <span class="main-nav" style="left:891px">JOBS</span>
  <span class="social" style="left:980px"></span>
  <span class="social" style="left:1012px"></span>
  <span class="social" style="left:1044px"></span>
</header>

<section class="hero" role="img" aria-label="Photo of a lecture hall with an audience listening to a speaker">
  <h1 class="hero-title">Data and Operations Networks</h1>
  <span class="btn" style="left:526px;top:125px;width:146px;height:40px;font-size:14px">Read more</span>
  <span class="dot" style="left:562px"></span>
  <span class="dot" style="left:578px"></span>
  <span class="dot active" style="left:595px"></span>
  <span class="dot" style="left:614px"></span>
  <span class="dot" style="left:631px"></span>
</section>

<section class="about">
  <div class="photo" role="img" aria-label="Photo of a seminar room with participants" style="left:137px;top:59px;width:298px;height:237px;background:linear-gradient(135deg,#c9c2b8,#7b6f62)"></div>
  <div class="photo" role="img" aria-label="Photo of a presentation in a meeting room" style="left:233px;top:190px;width:352px;height:237px;background:linear-gradient(135deg,#d8d4cc,#8a8378);box-shadow:0 2px 8px rgba(0,0,0,.2)"></div>
  <h2 class="section-title about-title">DATA AND OPERATIONS<br>NETWORKS (DKN)</h2>
  <p class="about-text">Chair in Commercial Studies, especially data and operations networks at Vellmoor University deals with the development and management of data-driven services, for instance healthcare. Directed by Prof. Dr.-Ing. Henrik Valdorf, the chair investigates how the application of experimental design methods combined with distributed, data analytic approaches lead to adaptive service designs and innovative solutions. This research is conducted in basic and applied research projects in cooperation with leading research and industry partners. Results are applied and validated in industry projects by the research group Smart Operations Engineering (SOE) at the Northfield Institute for Machine Intelligence (NIMI).</p>
  <span class="btn" style="left:640px;top:401px;width:106px;height:30px">Read more</span>
</section>

<section class="research">
  <h2 class="section-title abs" style="left:132px;top:68px">RESEARCH</h2>
  <ul class="caret-list" style="left:134px;top:140px">
    <li style="height:35px">Geschäfts- modelle &amp; KI</li>
    <li style="height:35px">Hybride Wertschöpf. &amp; KI</li>
    <li style="height:35px">Kompetenz - &amp; Wissensvermittl.</li>
    <li style="height:35px">AIOS-IOT</li>
    <li style="height:35px">Deep Learning in Sensor Datenströmen</li>
    <li style="height:35px">Responsible AI in UI</li>
  </ul>
  <span class="btn" style="left:134px;top:374px;width:106px;height:30px">Read more</span>
  <div class="photo" role="img" aria-label="Photo of two researchers presenting a food sample" style="left:621px;top:56px;width:352px;height:247px;background:linear-gradient(135deg,#e6e2dc,#8c7f70)"></div>
  <div class="photo" role="img" aria-label="Photo of a workshop audience in a green hall" style="left:718px;top:188px;width:350px;height:235px;background:linear-gradient(135deg,#9aa58c,#4f5749);box-shadow:0 2px 8px rgba(0,0,0,.2)"></div>
</section>

<section class="teaching">
  <h2 class="section-title abs" style="left:133px;top:52px">TEACHING</h2>
  <div class="field" style="left:380px;top:51px;width:421px;height:41px"><span>Course categories</span><svg width="10" height="6" viewBox="0 0 10 6"><path d="M0 0h10L5 6z" fill="#333"/></svg></div>
  <div class="field" style="left:818px;top:51px;width:250px;height:41px"><span>Search</span><svg width="12" height="12" viewBox="0 0 12 12"><circle cx="5" cy="5" r="3.8" fill="none" stroke="#555" stroke-width="1.4"/><path d="M8 8l3 3" stroke="#555" stroke-width="1.4"/></svg></div>
  <ul class="caret-list" style="left:134px;top:144px">
    <li style="height:42px">WS 20/21</li>
    <li style="height:41px">SoSe 21</li>
    <li>Teaching-Archive</li>
  </ul>
  <ul class="caret-list" style="left:389px;top:144px">
    <li style="height:42px">Learning Platform</li>
    <li style="height:41px">Theses</li>
    <li>Book Lending</li>
  </ul>
</section>

<section class="team">
  <h2 class="section-title abs" style="left:0;width:1200px;text-align:center;top:48px">TEAM</h2>
  <div class="abs" role="img" aria-label="Portrait photo of a research assistant" style="left:133px;top:130px;width:81px;height:81px;border-radius:50%;background:linear-gradient(135deg,#b7aca2,#5a524c)"></div>
  <span class="abs" style="left:239px;top:138px;font-size:22px;color:var(--link)">Research Assistants</span>
  <span class="abs" style="left:241px;top:172px;font-size:13px;color:#333">By Hiwis</span>
  <div class="abs" style="left:134px;top:228px;width:934px;height:2px;background:#d4d6da"></div>
  <h3 style="left:133px;top:256px">Description</h3>
  <p class="body" style="top:295px">Sed ut perspiciatis unde omnis iste natus error sit voluptatem accusantium doloremque laudantium, totam rem aperiam, eaque ipsa quae ab illo inventore veritatis et quasi architecto beatae vitae dicta sunt explicabo. Nemo enim ipsam voluptatem quia voluptas sit aspernatur aut odit aut fugit, sed quia consequuntur magni dolores eos qui ratione voluptatem sequi nesciunt. Neque porro quisquam est, qui dolorem ipsum quia dolor sit amet, consectetur, adipisci velit, sed quia non numquam eius modi tempora incidunt ut labore et dolore magnam aliquam quaerat voluptatem</p>
  <h3 style="left:133px;top:426px">Features</h3>
  <ul class="caret-list" style="left:134px;top:464px">
    <li style="height:28px;font-size:13px">Sed ut perspiciatis unde omnis iste natus error</li>
    <li style="height:28px;font-size:13px">But I must explain to you how all this</li>
    <li style="height:28px;font-size:13px">On the other hand, we denounce with</li>
    <li style="font-size:13px">when our power of choice is untrammelled</li>
  </ul>
  <p class="body" style="top:592px">Sed ut perspiciatis unde omnis iste natus error sit voluptatem accusantium doloremque laudantium, totam rem aperiam, eaque ipsa quae ab illo inventore veritatis et quasi architecto beatae vitae dicta sunt explicabo. Nemo enim ipsam voluptatem quia voluptas sit aspernatur aut odit aut fugit, sed quia consequuntur magni dolores eos qui ratione voluptatem sequi nesciunt. Neque porro quisquam est, qui dolorem ipsum quia dolor sit amet, consectetur, adipisci velit, sed quia non numquam eius modi tempora incidunt ut labore et dolore magnam aliquam quaerat voluptatem</p>
  <div class="contact-item" style="left:136px;top:733px">
    <span class="icon-circle"><svg width="14" height="14" viewBox="0 0 24 24"><path d="M6.6 10.8a15 15 0 0 0 6.6 6.6l2.2-2.2c.3-.3.7-.4 1-.2 1.1.4 2.3.6 3.6.6.6 0 1 .4 1 1V20c0 .6-.4 1-1 1A17 17 0 0 1 3 4c0-.6.4-1 1-1h3.5c.6 0 1 .4 1 1 0 1.3.2 2.5.6 3.6.1.3 0 .7-.2 1z" fill="#fff"/></svg></span>
    <span>Call Us<br>+49 (0) 555 018 2247 .</span>
  </div>
  <div class="contact-item" style="left:381px;top:733px">
    <span class="icon-circle"><svg width="14" height="12" viewBox="0 0 14 12"><rect x="0.5" y="1" width="13" height="10" rx="1" fill="#fff"/><path d="M1 2l6 4.5L13 2" fill="none" stroke="#1b3a72" stroke-width="1.3"/></svg></span>
    <span>E mail Us<br>info@dkn.uni-vellmoor.example</span>
  </div>
</section>

<section class="publications">
  <h2 class="section-title abs" style="left:131px;top:52px">PUBLICATIONS</h2>
  <span class="abs icon-circle" style="left:699px;top:51px;width:32px;height:32px"><svg width="18" height="14" viewBox="0 0 18 14"><path d="M9 1L1 5l8 4 8-4z" fill="#fff"/><path d="M4 7v3.5c0 1 2.2 2 5 2s5-1 5-2V7L9 9.5z" fill="#fff"/></svg></span>
  <div class="abs" style="left:739px;top:52px;width:329px;height:34px;background:#fff;border-radius:17px;display:flex;align-items:center;justify-content:space-between;padding:0 10px 0 16px">
    <svg width="12" height="12" viewBox="0 0 12 12"><circle cx="5" cy="5" r="3.8" fill="none" stroke="#555" stroke-width="1.4"/><path d="M8 8l3 3" stroke="#555" stroke-width="1.4"/></svg>
    <span style="width:18px;height:18px;border-radius:50%;background:#e4e5e8;font-size:10px;font-weight:700;display:flex;align-items:center;justify-content:center;color:#333">A</span>
  </div>
  <article class="pub-card" style="left:134px">
    <h4>Arvik, L., &amp; Valdorf, H.</h4>
    <p>An Adaptive Checkout Assistant Based On Shopper Context, Proceedings of the 12th Vellmoor Symposium on Data Networks, 2020.</p>
    <span class="pdf-tag">PDF (3.62 MB)</span>
  </article>
  <article class="pub-card" style="left:451px">
    <h4>Arvik, L., &amp; Valdorf, H.</h4>
    <p>Sensor-Driven Coaching for Active Lifestyles in Small Towns, Brightfield Mobile Health Workshop '20: Lessons from Community Health Programs for Remote Regions, 2020.</p>
    <span class="pdf-tag">PDF (3.62 MB)</span>
  </article>
  <article class="pub-card" style="left:769px">
    <h4>Ren, T.; Kessler, J.; Odell, B. &amp; Valdorf, H.</h4>
    <p>TRX : Tonal Range Indices for Rating the Visual Clarity of Processed Photographs, POSTER presentation at Kestrel Imaging Forum '20, 2019.</p>
    <span class="pdf-tag">PDF (3.62 MB)</span>
  </article>
</section>

<section class="projects">
  <h2 class="section-title abs" style="left:0;width:1200px;text-align:center;top:56px">PROJECTS</h2>
  <span class="proj-sub" style="left:132px">LIST OF PROJECTS</span>
  <span class="proj-sub" style="left:616px">LIST OF &nbsp;ARCHIVED PROJECTS</span>
  <div class="proj-box" style="left:134px">
    <div class="proj-item" style="top:30px"><h4>KORVALIS</h4><p>The innovation competition „Artificial Intelligence as a Driver for Economically Relevant Ecosystems"</p><a>READ MORE</a></div>
    <div class="proj-rule" style="top:130px"></div>
    <div class="proj-item" style="top:152px"><h4>PLONTIX</h4><p>Digitalization represents an opportunity for food industry to increase efficiency by using internal and external data.</p><a>READ MORE</a></div>
    <div class="proj-rule" style="top:253px"></div>
    <div class="proj-item" style="top:275px"><h4>VORDENSYS</h4><p>The booming e-commerce and the advancing digitalization demand the stationary trade.</p><a>READ MORE</a></div>
  </div>
  <div class="proj-box" style="left:617px">
    <div class="proj-item" style="top:30px"><h4>FIELDNET WORLD</h4><p>The objective of the research project FINEW is to create a manufacturer-independent and thus fully compatible network</p><a>READ MORE</a></div>
    <div class="proj-rule" style="top:130px"></div>
    <div class="proj-item" style="top:152px"><h4>GROWCAST</h4><p>The project GrowCast is dedicated to creating a prediction model which can predict fertilizer prices.</p><a>READ MORE</a></div>
    <div class="proj-rule" style="top:253px"></div>
    <div class="proj-item" style="top:275px"><h4>PLANNING GRANT „PREDICTING BIASES</h4><p>Our intended project will identify key questions related to modeling cognitive biases and how they affect</p><a>READ MORE</a></div>
  </div>
</section>

<section class="news">
  <h2 class="section-title abs" style="left:0;width:1200px;text-align:center;top:48px">LATEST NEWS</h2>
  <article class="news-card" style="left:134px">
    <div class="photo" role="img" aria-label="Photo of a professor arranging a row of dominoes" style="background:linear-gradient(135deg,#e9e9e9,#8e8e8e)"></div>
    <div class="news-body"><div class="news-date">30.03.2021</div><h4>Smart data for smarter decisions: How AI is helping industrial production run more smoothly</h4><p>Using artificial intelligence to prevent production downtime: Professor Henrik Valdorf</p></div>
    <span class="btn" style="left:22px;top:340px;width:84px;height:24px;font-size:10px">Read more</span>
  </article>
  <article class="news-card" style="left:451px">
    <div class="photo" role="img" aria-label="Photo of a professor holding a box labelled smart data" style="background:linear-gradient(135deg,#f0f0f0,#9a9a9a)"></div>
    <div class="news-body"><div class="news-date">30.03.2021</div><h4>Lindenfeld Fair: How artificial intelligence is helping make food production smarter</h4><p>Smart data packages are providing food producers with greater insight, making production...</p></div>
    <span class="btn" style="left:22px;top:340px;width:84px;height:24px;font-size:10px">Read more</span>
  </article>
  <article class="news-card" style="left:769px">
    <div class="photo" role="img" aria-label="Title slide of a conference paper presentation" style="background:linear-gradient(180deg,#f5f5f5,#d9d9de)"></div>
    <div class="news-body"><div class="news-date">13-16 December 2020</div><h4>International Conference on Data Networks (ICDN) 2020: Presentation of Lena Arvik and Professor Henrik Valdorf' paper</h4><p>The annual International Conference on</p></div>
    <span class="btn" style="left:22px;top:340px;width:84px;height:24px;font-size:10px">Read more</span>
  </article>
</section>

<section class="jobs">
  <div class="photo" role="img" aria-label="Photo of a speaker presenting to an audience in a brick hall" style="left:43px;top:37px;width:605px;height:479px;background:linear-gradient(135deg,#8a8fb5,#3c3b52 60%,#2a2a35)"></div>
  <h2 class="section-title abs" style="left:719px;top:114px">JOBS AND INTERNSHIP</h2>
  <p class="jobs-text">At vero eos et accusamus et iusto odio dignissimos ducimus qui blanditiis praesentium voluptatum deleniti atque corrupti quos dolores et quas molestias excepturi sint occaecati cupiditate non provident, similique sunt in culpa qui officia deserunt mollitia animi, id est laborum et dolorum fuga. Et harum quidem rerum facilis est et expedita distinctio. Nam libero tempore, cum soluta nobis est eligendi optio cumque nihil impedit quo</p>
  <span class="btn" style="left:719px;top:405px;width:137px;height:38px;font-size:14px">Apply Job</span>
</section>

<footer class="site-footer">
  <div class="brand" style="left:166px;top:82px"><span class="brand-dot" style="width:46px;height:46px;background:#fff"></span><span class="brand-name" style="color:#fff;font-size:36px">DKN</span></div>
  <span class="footer-head" style="left:435px">CONTACT</span>
  <p class="footer-text" style="left:435px;top:89px;width:250px">You can find us in building C2 7, 2nd level on the campus of Vellmoor University.</p>
  <p class="footer-text" style="left:435px;top:138px;width:250px">Office hours including lending of books happen on request</p>
  <p class="footer-text" style="left:435px;top:187px;width:250px">office@dkn.uni-vellmoor.example or via phone +49 (0) 555 018 2247 .</p>
  <span class="footer-head" style="left:802px">MENU</span>
  <ul class="footer-menu" style="left:802px;top:86px">
    <li>Research</li><li>Learning-Platform</li><li>Teaching</li><li>Team</li><li>Publications</li>
  </ul>
  <ul class="footer-menu" style="left:976px;top:86px">
    <li>Jobs</li><li>Projects</li><li>Events</li><li>Cooperations</li>
  </ul>
  <p class="copyright">Copyright © 2021 All Rights Reserved</p>
</footer>

</body>
</html>
```